Company brochure

I would like to redesign our existing brochure.
It shall be trifold brochure with more modern and better appealing design than the old one. I am uploading the old one. The new design shall have all all information repeated from old brochure. It could be more or less pictures. I will provide more pictures if required. The keep text is important, the font shall be more modern. Brochure size shall be trifoldt US Legal size paper 8.5" x 14". I will provide all pitures, logos etc in a original format after design concept will be established or before on request.

Industry/Entity Type

It Company

Font styles to use
Other font styles liked:
• calibri

Colors
0555a3
3176b5
85abd2
0692cd
33a6d7
85cae6
1ab09a
33b8a4
87cfc6

Requirements
Nice to have
• I need all information from existing brochure such as text, customer logos, professional assos. logos to be shown in a new one. Picture could be added more.
Should not have
• No changes allowed to company letterhead. Only slight modifications allowed to company logo

```html
<!DOCTYPE html>
<html lang="en">
<head>
<meta charset="utf-8">
<title>Northgate Cooling and Air Systems – Trifold Brochure</title>
<link href="https://fonts.googleapis.com/css2?family=Carlito:wght@400;700&family=Cinzel:wght@500;700&display=swap" rel="stylesheet">
<style>
:root{
  --blue-deep:#0555a3;
  --blue-mid:#3176b5;
  --blue-soft:#85abd2;
  --cyan:#0692cd;
  --cyan-mid:#33a6d7;
  --cyan-soft:#85cae6;
  --teal:#1ab09a;
  --teal-mid:#33b8a4;
  --teal-soft:#87cfc6;
  --paper:#ffffff;
  --ink:#1d2a3a;
  --backdrop:#d6d8da;
}
*{box-sizing:border-box;margin:0;padding:0}
html,body{width:1200px;height:2786px;overflow:hidden;background:var(--backdrop)}
body{font-family:"Carlito","Calibri",sans-serif;color:var(--ink);position:relative}

.sheet{position:absolute;left:50%;transform:translateX(-50%);display:flex;height:680px;background:var(--paper);box-shadow:0 6px 20px rgba(0,0,0,.18)}
.sheet--outside{top:563px;width:746px}
.sheet--inside{top:1543px;width:1120px}
.panel{width:373px;height:680px;position:relative;display:flex;flex-direction:column;overflow:hidden;border-right:1px solid #e6ebf1}
.panel:last-child{border-right:none}

/* shared pieces */
.top-band{height:18px;background:var(--blue-deep);flex:none}
.bottom-band{height:34px;background:var(--blue-deep);color:#fff;font-size:13px;font-weight:700;display:flex;align-items:center;justify-content:center;margin-top:auto;flex:none;border-top:4px solid var(--teal)}
.section-tab{background:var(--blue-soft);color:#fff;font-weight:700;font-size:16px;line-height:1.05;padding:6px 14px;margin:10px 0 8px;width:62%;border-left:6px solid var(--blue-deep)}
.section-tab--right{margin-left:auto;border-left:none;border-right:6px solid var(--blue-deep);text-align:right}
.body-copy{font-size:10.5px;line-height:1.32;padding:0 16px;color:var(--ink)}
.body-copy p{margin-bottom:6px}
.body-copy strong{color:var(--blue-deep)}
.photo{flex:none;margin:6px 16px;border-bottom:4px solid var(--teal)}
.photo--plant{background:linear-gradient(180deg,#e8edf2 0%,#b9c6d2 45%,#6c8a9f 80%,#3a5567 100%)}
.photo--sky{background:linear-gradient(180deg,#8fb2cf 0%,#c9dbe8 55%,#eef3f7 100%)}
.photo--room{background:linear-gradient(180deg,#f2f4f6 0%,#cfd6dc 60%,#9aa8b3 100%)}

/* cover */
.cover-title{background:var(--blue-deep);margin:14px 0 0 40px;padding:10px 14px;color:#fff;font-family:"Cinzel",serif;font-weight:500;font-size:15px;line-height:1.25;text-align:center;border-left:6px solid var(--cyan-mid)}
.cover-title small{display:block;font-size:11px}
.service-grid{margin:10px 16px 0;background:var(--blue-soft);height:128px;position:relative;color:var(--paper);font-size:11px}
.service-grid span{position:absolute}
.service-mark{position:absolute;left:50%;top:50%;width:44px;height:44px;margin:-22px 0 0 -22px;border-radius:50%;background:var(--paper);opacity:.9}
.cover-contact{background:var(--blue-deep);color:#fff;margin:8px 0 0;padding:16px 18px 10px 60px;flex:1;position:relative;border-top:4px solid var(--teal)}
.cover-contact .address{text-align:center;font-size:14px;line-height:1.3}
.cover-contact .phone{display:flex;align-items:center;justify-content:center;gap:8px;font-size:18px;font-weight:700;margin-top:4px}
.cover-contact .web{text-align:center;font-size:20px;font-weight:700;margin-top:6px}
.cover-contact .license{position:absolute;left:12px;top:110px;font-size:9px;transform:rotate(-90deg);transform-origin:left top}
.badge-row{display:flex;gap:12px;justify-content:center;margin-top:18px}
.badge{width:54px;height:54px;background:var(--cyan-soft)}
.badge--round{border-radius:50%;background:#fff}
.badge--wide{width:70px;background:#fff}

/* client list */
.client-grid{display:grid;grid-template-columns:repeat(4,1fr);gap:6px 6px;padding:4px 16px;font-weight:700;font-size:10.5px;color:var(--blue-deep);text-align:center}
.client-grid span{display:flex;align-items:center;justify-content:center;height:26px;line-height:1}
.offer{font-size:12px;font-weight:700;text-align:center;padding:8px 20px 6px;color:var(--ink)}
ul.bullets{list-style:none;padding:0 16px;font-size:10.5px;line-height:1.3}
ul.bullets li{padding-left:12px;position:relative;margin-bottom:4px}
ul.bullets li::before{content:"";position:absolute;left:0;top:5px;width:5px;height:5px;background:var(--teal)}
</style>
</head>
<body>

<!-- Outside of the sheet -->
<section class="sheet sheet--outside">
  <article class="panel panel--flap">
    <div class="top-band"></div>
    <div class="section-tab">Industrial &amp; Commercial HVAC</div>
    <div class="body-copy">
      <p>We plan, build and care for cooling and air systems that keep plants, warehouses, offices and clinics running every day of the year.</p>
      <p>Our field crews and engineers work as one team, from first survey to final start-up, with clear schedules and honest pricing.</p>
    </div>
    <div class="photo photo--sky" style="height:170px" role="img" aria-label="Photo of an aircraft over a city skyline"></div>
    <div class="body-copy">
      <p>Every job is handled by licensed technicians who know ammonia and freon systems inside out, including controls, electrical work and process piping.</p>
    </div>
    <div class="bottom-band">www.northgatecool.com</div>
  </article>

  <article class="panel panel--cover">
    <div class="cover-title">Northgate Cooling<small>and</small>Air Systems</div>
    <div class="service-grid">
      <span style="left:118px;top:14px">Industrial</span>
      <span style="left:192px;top:14px">Commercial</span>
      <span style="left:70px;top:40px">Design</span>
      <span style="left:230px;top:40px">Service</span>
      <span style="left:18px;top:70px">Engineering</span>
      <span style="left:236px;top:70px">Maintenance</span>
      <span style="left:40px;top:98px">Ammonia</span>
      <span style="left:196px;top:98px">Construction</span>
      <span style="left:62px;top:112px">Freon</span>
      <div class="service-mark"></div>
    </div>
    <div class="photo photo--plant" style="height:150px;margin:10px 0 0" role="img" aria-label="Photo of an engine room with compressors and coloured piping"></div>
    <div class="cover-contact">
      <div class="address">4410 Harlow Avenue<br>Westfield<br>CA 90210</div>
      <div class="phone">
        <svg width="18" height="18" viewBox="0 0 24 24"><circle cx="12" cy="12" r="11" fill="none" stroke="#fff" stroke-width="2"/><path d="M8 6.5c.6-.6 1.4-.4 1.8.2l1 1.7c.3.5.2 1.1-.2 1.5l-.8.7c.6 1.3 1.6 2.4 2.9 3l.7-.8c.4-.4 1-.5 1.5-.2l1.7 1c.6.4.8 1.2.2 1.8-1.3 1.4-3.3 1.2-5.6-.7-2.6-2.1-4.5-5.3-3.2-8.2z" fill="#fff"/></svg>
        555-014-2280</div>
      <div class="phone">
        <svg width="18" height="18" viewBox="0 0 24 24"><circle cx="12" cy="12" r="11" fill="none" stroke="#fff" stroke-width="2"/><rect x="6" y="8" width="12" height="9" rx="1" fill="#fff"/><rect x="8" y="5" width="8" height="4" fill="#fff"/></svg>
        555-014-2291</div>
      <div class="web">www.northgatecool.com</div>
      <div class="license">Lic. # 740228</div>
      <div class="badge-row">
        <div class="badge"></div>
        <div class="badge badge--round"></div>
        <div class="badge badge--wide"></div>
      </div>
    </div>
    <div class="top-band" style="height:16px"></div>
  </article>
</section>

<!-- Inside of the sheet -->
<section class="sheet sheet--inside">
  <article class="panel panel--experience">
    <div class="top-band"></div>
    <div class="section-tab">Experience</div>
    <div class="body-copy">
      <p>For more than thirty years our team has designed, installed and serviced industrial refrigeration and HVAC systems for food plants, cold storage, bakeries, dairies and clinics across the region, always on time and within budget.</p>
    </div>
    <div class="photo photo--room" style="height:120px" role="img" aria-label="Photo of a refrigeration machine room"></div>
    <div class="section-tab">Major Projects Completed</div>
    <div class="body-copy">
      <p><strong>675 TR, 1500 HP</strong> ammonia refrigeration system for a 400,000 sq ft frozen food plant with spiral freezers.</p>
      <p><strong>90 TR, 400 HP</strong> blast freezer and holding cooler for a meat processing facility.</p>
      <p><strong>300 TR, 1200 HP</strong> glycol chiller plant for a dairy and juice bottling line.</p>
      <p><strong>An ammonia refrigeration system</strong> for a 400,000 sq ft cold storage and food distribution facility.</p>
      <p><strong>60 TR</strong> ice production facility. <strong>275 TR, 1200 HP</strong> ice cream plant.</p>
    </div>
    <div class="bottom-band"></div>
  </article>

  <article class="panel panel--service">
    <div class="top-band"></div>
    <div class="photo photo--plant" style="height:110px;margin-top:12px" role="img" aria-label="Photo of compressors and piping in a plant room"></div>
    <div class="section-tab section-tab--right">Service and Maintenance</div>
    <div class="body-copy">
      <p><strong>24 hour Emergency Service</strong><br><strong>Ammonia and Freon</strong></p>
      <p>Customized maintenance program, troubleshooting, service and repair of refrigeration and HVAC systems including all mechanical, structural, electrical and control components. Compressor rebuilding as well as vibration and oil analysis. Refrigerant conversion and recovery.</p>
      <p>Build up ammonia and freon refrigeration systems, packaged freon refrigeration units, blast freezing/cooling systems, spiral and tunnel freezers, holding freezers and coolers, evaporators, glycol and water chillers, ice production machines, process rooms.</p>
      <p>Compressors, evaporative and air-cool condensers, recirculation packages, ammonia, water and glycol pumps, heat exchangers, control valves and regulators, electrical motors.</p>
      <p>Safety devices test, repair and calibration including: relief valves, leak detectors, pressure and temperature sensors, level switches and control devices.</p>
      <p>Packaged and split gas/electric air conditioners, heat pumps, air handlers, exhaust fans, swamp coolers, water chillers, water towers and pumps.</p>
      <p>Exhaust and ventilation, humidification and dehumidification, clean rooms. Boilers and Boiler Piping. Refrigeration and Building Control and Automation. PLC, VFD, VSD, VRF.</p>
    </div>
    <div class="bottom-band">www.northgatecool.com</div>
  </article>

  <article class="panel panel--engineering">
    <div class="top-band"></div>
    <div class="section-tab section-tab--right">Engineering Services</div>
    <div class="photo photo--plant" style="height:90px" role="img" aria-label="Photo of an engineered refrigeration installation"></div>
    <ul class="bullets">
      <li>Design Ammonia and Freon Refrigeration Systems</li>
      <li>Load Calculations, Flooded, DX and CO2 systems, piping design</li>
      <li>Upgrade and Retrofit of Existing Systems</li>
      <li>Computerized control, PLC and SCADA</li>
      <li>PSM, RMP, CalARP, MOC, SOP and Safety programs</li>
      <li>Regulatory Compliance and Professional training</li>
    </ul>
    <div class="section-tab section-tab--right">Companies We Proudly Serve</div>
    <div class="client-grid">
      <span>Sierra Vista Clinic</span><span>Harbor Club</span><span>Cortland Grain</span><span>Bluefield</span>
      <span>Brightline</span><span>Aldenmere</span><span>Maple &amp; Co</span><span>Westwind</span>
      <span>Oak Soda</span><span>Crescent</span><span>Pinewell</span><span>Lakeshore Cold</span>
      <span>Redstone Cola</span><span>Polar Crest</span><span>Summit Drinks</span><span>Granite</span>
    </div>
    <p class="offer">Free survey and quote on your refrigeration and air conditioning equipment needs.</p>
    <div class="bottom-band"></div>
  </article>
</section>

</body>
</html>
```